Time Clock Banner Ads

We are in the time and attendance industry. This is basically "bundy clocks" and software.

We need 10 - 12 banners designed each with a common themed background but each with two custom images which I will provide.

I think it likely that a price will need to be negotiated to accommodate providing 12 variations around the basic design.

These banners will display different product solution alternatives and will be used on a website with product specific pages. They will not be company branded.

The banner should be designed in 1024 * 768 resolution

Your submitted banner design will include:-
1) A time and attendance themed background (which you will provide).

2) Two images attached.

3) The text "Your customised Time and Attendance System"

4) A click for more information button. This will be removed from the final design for each banner and provided as a separate graphic.

Design guide

The product is technical in nature
Biometrics are a product feature
This will be embedded on a few sites so it is not possible to provide guidance on existing colours and schemes.

We like blue colours but we are open to colours schemes which may be considered neutral and easy to incorporate into other website themes.

The attached images show and Bivorin8 time clock and an image from the KRV2 Software. These images were pulled from a web search. You may want to find images that suit your design better.

```html
<!DOCTYPE html>
<html lang="en">
<head>
<meta charset="utf-8">
<title>Your Customised Time and Attendance System</title>
<link rel="stylesheet" href="https://fonts.googleapis.com/css2?family=Archivo+Black&family=Arimo:wght@700&display=swap">
<style>
  :root {
    --navy-deep: #06325f;
    --navy: #0c4478;
    --navy-light: #2a5f92;
    --shadow: #021a36;
    --white: #ffffff;
    --photo-light: #eef1f4;
    --photo-mid: #c9d1da;
    --photo-dark: #8a97a6;
    --rim: #d6477a;
    --button-top: #ee6a93;
    --button-bottom: #c83364;
  }
  html, body {
    margin: 0;
    padding: 0;
    width: 1200px;
    height: 900px;
    overflow: hidden;
    background: #161616;
  }
  .banner {
    position: relative;
    width: 1200px;
    height: 900px;
    overflow: hidden;
  }
  .banner svg { display: block; }
  .headline-heavy {
    font-family: "Archivo Black", "Arial Black", sans-serif;
    fill: var(--white);
  }
  .headline-bold {
    font-family: "Arimo", Arial, sans-serif;
    font-weight: 700;
    fill: var(--white);
  }
  .button-label {
    font-family: "Arimo", Arial, sans-serif;
    font-weight: 700;
    fill: var(--white);
    font-size: 17px;
  }
</style>
</head>
<body>
<main class="banner">
  <svg width="1200" height="900" viewBox="0 0 1200 900" xmlns="http://www.w3.org/2000/svg">
    <defs>
      <linearGradient id="bg-fill" x1="0" y1="0" x2="0.3" y2="1">
        <stop offset="0" stop-color="#0a3c70"/>
        <stop offset="1" stop-color="var(--navy-deep)"/>
      </linearGradient>
      <radialGradient id="clock-glow" cx="0.5" cy="0.5" r="0.5">
        <stop offset="0" stop-color="var(--navy-light)" stop-opacity="0.45"/>
        <stop offset="1" stop-color="var(--navy-light)" stop-opacity="0"/>
      </radialGradient>
      <linearGradient id="table-fade" x1="0" y1="0" x2="0" y2="1">
        <stop offset="0" stop-color="#3b6ea1" stop-opacity="0.35"/>
        <stop offset="1" stop-color="#3b6ea1" stop-opacity="0"/>
      </linearGradient>
      <linearGradient id="photo-fill" x1="0" y1="0" x2="0.4" y2="1">
        <stop offset="0" stop-color="var(--photo-light)"/>
        <stop offset="0.55" stop-color="var(--photo-mid)"/>
        <stop offset="1" stop-color="var(--photo-dark)"/>
      </linearGradient>
      <linearGradient id="button-fill" x1="0" y1="0" x2="0" y2="1">
        <stop offset="0" stop-color="var(--button-top)"/>
        <stop offset="1" stop-color="var(--button-bottom)"/>
      </linearGradient>
      <filter id="text-shadow" x="-10%" y="-10%" width="130%" height="140%">
        <feDropShadow dx="5" dy="6" stdDeviation="2" flood-color="var(--shadow)" flood-opacity="0.85"/>
      </filter>
    </defs>

    <!-- background -->
    <rect class="backdrop" width="1200" height="900" fill="url(#bg-fill)"/>
    <rect class="backdrop-table" role="img" aria-label="Faint attendance software table behind the headline" x="0" y="0" width="1200" height="300" fill="url(#table-fade)"/>
    <circle class="backdrop-clock" role="img" aria-label="Faint clock face decoration" cx="900" cy="1050" r="420" fill="url(#clock-glow)"/>

    <!-- product photo disc -->
    <circle class="photo-rim" cx="1032" cy="322" r="418" fill="var(--rim)"/>
    <circle class="photo-disc" role="img" aria-label="Fingerprint time clock terminal in front of an attendance software spreadsheet" cx="1024" cy="312" r="412" fill="url(#photo-fill)"/>

    <!-- headline -->
    <g class="headline" filter="url(#text-shadow)">
      <text class="headline-heavy" x="45" y="162" font-size="115" textLength="342" lengthAdjust="spacingAndGlyphs">YOUR</text>
      <text class="headline-bold" x="97" y="263" font-size="95" textLength="488" lengthAdjust="spacingAndGlyphs">CUSTOMISED</text>
      <text class="headline-heavy" x="52" y="439" font-size="188" textLength="527" lengthAdjust="spacingAndGlyphs">TIME</text>
      <text class="headline-bold" x="254" y="513" font-size="58" textLength="108" lengthAdjust="spacingAndGlyphs">and</text>
      <text class="headline-bold" x="40" y="623" font-size="110" textLength="605" lengthAdjust="spacingAndGlyphs">ATTENDANCE</text>
      <text class="headline-bold" x="356" y="736" font-size="95" textLength="320" lengthAdjust="spacingAndGlyphs">SYSTEM</text>
    </g>

    <!-- call to action -->
    <g class="more-info-button">
      <rect x="95" y="790" width="205" height="58" rx="10" fill="url(#button-fill)"/>
      <text class="button-label" x="158" y="814" text-anchor="middle">More</text>
      <text class="button-label" x="158" y="834" text-anchor="middle">Information</text>
      <path d="M264 806 L278 819 L264 832" fill="none" stroke="var(--white)" stroke-width="5" stroke-linecap="round" stroke-linejoin="round"/>
    </g>
  </svg>
</main>
</body>
</html>
```